Business Card Design/Stationary Design

We would like designers to submit cool, hip business card designs (plus stationary designs) for a new, upstart software development company located in Toronto.
If you have any questions, please email us.
For inspiration on designs:
http://cardmuse.example/cool-business-cards/
http://layoutnotes.example/2008/05/36-cool-business-cards-you-should%E2%80%99ve-seen.html
http://gigharbor.example/general/18-smokin-hot-business-card-designs/

Card info:

Selvakumar (Selv) Nadarasan

Founder and CEO

47 Brindle Court, Suite 311

Toronto, ON M4K 2T8

Phone: 647-512-7730

Mobile: 416-273-5094

Fax: 647-512-7731

Email: selvakumar.nadarasan@mailbrook.example

www.quendrix.example
Updates

Hi everyone,

In terms of all the designs I have seen so far, here is what I like:

1.  I really like the "back" part of this design.  The "front" looks pretty decent as well, but for the "front", look at #2 on this list.  I like that.

http://www.pitchboard.example/image.aspx?imageLocation=1000_10001_2000_image.jpg&type=design300px&whiteLabelCustId=9999

2. "Side 1" of this I like, the front needs to be reworked.

http://www.pitchboard.example/image.aspx?imageLocation=1000_10002_2000_image.png&type=design300px&whiteLabelCustId=9999

3. http://www.pitchboard.example/image.aspx?imageLocation=1000_10003_2000_image.jpg&type=design300px&whiteLabelCustId=9999

4. http://www.pitchboard.example/image.aspx?imageLocation=1000_10004_2000_image.jpg&type=design300px&whiteLabelCustId=9999

Target Market(s)

We are focused on enterprise customers right now, so businesses with a long-term goal of also reaching out to the consumer market as well.

Industry/Entity Type

Software

Requirements
Must have
• Must look cool, ultra-modern, clean and eye-catching. Must incorporate our logo and the colors found in the logo.

```html
<!DOCTYPE html>
<html lang="en">
<head>
<meta charset="utf-8">
<title>Quendrix Technologies Inc. — Business Card</title>
<link rel="stylesheet" href="https://fonts.googleapis.com/css2?family=Source+Sans+3:wght@300;700&family=Questrial&display=swap">
<style>
  :root {
    --page-bg: #ffffff;
    --label-grey: #8a8a8a;
    --front-green: #86e02a;
    --front-ink: #0a0a0a;
    --back-black: #000000;
    --back-glow: #7ce82c;
    --brand-lime: #c8f000;
    --brand-lime-soft: #d6ef7a;
    --mark-light: #b8f000;
    --mark-mid: #6fd61e;
    --mark-deep: #3f8f10;
  }
  * { box-sizing: border-box; margin: 0; padding: 0; }
  html, body {
    width: 1200px;
    height: 812px;
    overflow: hidden;
    background: var(--page-bg);
  }
  .canvas {
    position: relative;
    width: 1200px;
    height: 812px;
  }
  .side-label {
    position: absolute;
    top: 2px;
    font-family: "Source Sans 3", Arial, sans-serif;
    font-weight: 300;
    font-size: 30px;
    color: var(--label-grey);
  }
  .side-label--front { left: 0; }
  .side-label--back { left: 688px; top: 6px; }

  .card {
    position: absolute;
    top: 57px;
    height: 751px;
    overflow: hidden;
  }

  /* Front */
  .card--front {
    left: 0;
    width: 525px;
    background: var(--front-green);
    border: 2px solid #111;
    box-shadow: inset 0 0 34px 10px rgba(0,0,0,0.85);
    color: var(--front-ink);
    font-family: "Source Sans 3", "Myriad Pro", Arial, sans-serif;
    font-weight: 700;
    text-align: center;
  }
  .contact-line {
    position: absolute;
    left: 0;
    right: 0;
    font-size: 28px;
    line-height: 1;
    white-space: nowrap;
  }
  .contact-name { top: 56px; font-size: 36px; }
  .contact-title { top: 100px; font-size: 25px; }
  .contact-address { top: 203px; }
  .contact-city { top: 259px; }
  .contact-phone { top: 317px; }
  .contact-mobile { top: 373px; }
  .contact-fax { top: 429px; }
  .contact-email { top: 487px; font-size: 24px; letter-spacing: -0.2px; }
  .contact-web { top: 543px; font-size: 25px; }

  .brand {
    position: absolute;
    left: 0;
    right: 0;
    text-align: center;
    font-family: "Questrial", "Century Gothic", sans-serif;
    font-weight: 400;
  }
  .brand-name {
    top: 620px;
    font-size: 80px;
    line-height: 1;
    letter-spacing: 1px;
  }
  .brand-subtitle {
    top: 707px;
    font-size: 16px;
    letter-spacing: 1.5px;
  }
  .card--front .brand { color: var(--front-ink); }
  .card--front .brand-subtitle { font-family: "Source Sans 3", Arial, sans-serif; font-weight: 700; }

  /* Back */
  .card--back {
    left: 670px;
    width: 530px;
    background: var(--back-black);
    border: 3px solid var(--back-glow);
    box-shadow: inset 0 0 26px 12px rgba(124,232,44,0.9);
  }
  .brand-mark-area {
    position: absolute;
    left: 92px;
    top: 120px;
    width: 340px;
    height: 340px;
    background: linear-gradient(135deg, var(--mark-mid) 0%, var(--mark-light) 55%, var(--mark-deep) 100%);
    opacity: 0.85;
  }
  .card--back .brand-name { color: var(--brand-lime); }
  .card--back .brand-subtitle { color: var(--brand-lime-soft); font-size: 15px; letter-spacing: 2px; top: 702px; }
</style>
</head>
<body>
<main class="canvas">
  <p class="side-label side-label--front">Business Card: Front</p>
  <p class="side-label side-label--back">Business Card: Back</p>

  <section class="card card--front" aria-label="Business card front">
    <p class="contact-line contact-name">Selvakumar (Selv) Nadarasan</p>
    <p class="contact-line contact-title">Founder and CEO</p>
    <p class="contact-line contact-address">47 Brindle Court, Suite 311</p>
    <p class="contact-line contact-city">Toronto, ON M4K 2T8</p>
    <p class="contact-line contact-phone">Phone: 647-512-7730</p>
    <p class="contact-line contact-mobile">Mobile: 416-273-5094</p>
    <p class="contact-line contact-fax">Fax: 647-512-7731</p>
    <p class="contact-line contact-email">selvakumar.nadarasan@mailbrook.example</p>
    <p class="contact-line contact-web">www.quendrix.example</p>
    <p class="brand brand-name">Quendrix</p>
    <p class="brand brand-subtitle">TECHNOLOGIES INC.</p>
  </section>

  <section class="card card--back" aria-label="Business card back">
    <div class="brand-mark-area" role="img" aria-label="Area for the Quendrix brand symbol in lime and green tones"></div>
    <p class="brand brand-name">Quendrix</p>
    <p class="brand brand-subtitle">TECHNOLOGIES INC.</p>
  </section>
</main>
</body>
</html>
```